VelloPath Business Card

Our company is called VelloPath and we are based in Tel Aviv, Israel. We create innovative and exciting methods for getting people on the web engaged with content. We need a cool yet professional business card that will represent our management level employees. keep in mind this is a start up company with a young atmosphere. You can be inspired by our logo (file attached, make sure you have the right font "Ubuntu-Condensed") Use the colors that are used in the logo and create a colourful and professional business card.

```html
<!DOCTYPE html>
<html lang="en">
<head>
<meta charset="utf-8">
<title>VelloPath Business Card</title>
<link rel="stylesheet" href="https://fonts.googleapis.com/css2?family=Ubuntu+Condensed&family=Open+Sans+Condensed:wght@300&display=swap">
<style>
  :root {
    --backdrop: #2a2a2c;
    --card: #ffffff;
    --ink: #2b2b2b;
    --blue: #2f8fd0;
    --pink: #e7297f;
    --purple: #8b2f8e;
    --yellow: #f7d21e;
    --orange: #f7a533;
    --green: #8cc63f;
    --sky: #4fb3e3;
  }
  * { margin: 0; padding: 0; box-sizing: border-box; }
  html, body { width: 1200px; height: 900px; overflow: hidden; }
  body {
    background: var(--backdrop);
    font-family: "Ubuntu Condensed", "Arial Narrow", sans-serif;
    color: var(--ink);
    position: relative;
  }
  .card {
    position: absolute;
    top: 296px;
    width: 540px;
    height: 308px;
    background: var(--card);
    overflow: hidden;
  }
  .card--front { left: 40px; }
  .card--back { left: 620px; }

  .front-mark {
    position: absolute;
    inset: 0;
    display: flex;
    align-items: center;
    justify-content: center;
    gap: 16px;
  }
  .front-mark__dot {
    width: 34px; height: 34px; border-radius: 50%;
    background: var(--pink);
  }
  .front-mark__name {
    font-size: 64px;
    color: var(--ink);
    letter-spacing: 0.5px;
  }

  .back-frame {
    position: absolute;
    inset: 0;
    background: linear-gradient(120deg, var(--purple), var(--pink) 20%, var(--yellow) 38%, var(--sky) 55%, var(--green) 72%, var(--orange) 86%, var(--purple));
    opacity: 0.85;
  }
  .back-panel {
    position: absolute;
    inset: 20px;
    background: var(--card);
    padding: 28px 34px;
  }
  .back-mark {
    display: flex;
    align-items: center;
    gap: 10px;
  }
  .back-mark__dot {
    width: 20px; height: 20px; border-radius: 50%;
    background: var(--pink);
  }
  .back-mark__name { font-size: 38px; color: var(--blue); }

  .back-details {
    display: flex;
    justify-content: space-between;
    margin-top: 34px;
  }
  .company { font-size: 14px; line-height: 1.45; }
  .company__name { color: var(--blue); font-size: 17px; letter-spacing: 0.5px; }
  .person__name { color: var(--blue); font-size: 22px; }
  .person__role { font-size: 14px; margin-bottom: 14px; }
  .contact { list-style: none; font-size: 14px; line-height: 1.6; }
  .contact li { display: flex; align-items: center; gap: 8px; }
  .contact svg { width: 12px; height: 12px; flex: none; }
</style>
</head>
<body>
  <section class="card card--front" aria-label="Card front">
    <div class="front-mark">
      <span class="front-mark__dot"></span>
      <span class="front-mark__name">VelloPath</span>
    </div>
  </section>

  <section class="card card--back" aria-label="Card back">
    <div class="back-frame" role="img" aria-label="Border of scattered multicoloured dots"></div>
    <div class="back-panel">
      <div class="back-mark">
        <span class="back-mark__dot"></span>
        <span class="back-mark__name">VelloPath</span>
      </div>
      <div class="back-details">
        <address class="company" style="font-style:normal">
          <div class="company__name">VELLOPATH</div>
          Suite 40, Harbor Lane,<br>
          Next to River Plaza, NY 10452
        </address>
        <div class="person">
          <div class="person__name">Daniel Orsen</div>
          <div class="person__role">Director</div>
          <ul class="contact">
            <li><svg viewBox="0 0 12 12"><rect x="3" y="0.5" width="6" height="11" rx="1" fill="none" stroke="#f7a533" stroke-width="1.2"/></svg>112-555-0147</li>
            <li><svg viewBox="0 0 12 12"><rect width="12" height="12" fill="#8b2f8e"/><path d="M1 3l5 4 5-4" fill="none" stroke="#fff" stroke-width="1.2"/></svg>d.orsen@mailbox.com</li>
            <li><svg viewBox="0 0 12 12"><circle cx="6" cy="6" r="5.5" fill="#8cc63f"/><path d="M0.5 6h11M6 0.5v11" stroke="#fff" stroke-width="1"/></svg>www.vellopath.com</li>
          </ul>
        </div>
      </div>
    </div>
  </section>
</body>
</html>
```